Store Front Sign for Vape Store

Interested in getting a store front sign graphic done. Sign is for over the door (lighted sign). Dimensions of sign: 6 feet long x 2 feet high.
Sign is for a Vape Store. I have attached the logo to be used.
Looking for a modern and professional look
Phone numbers to be used.
Whatsapp# 364-9105
Contact #593-6148
Sign should have Instagram & Facebook logos and. handle @mistralhaze

Industry/Entity Type

Vape | Electronic Cigarettes

Colors

Designer to choose colors to be used in the design.

Requirements
Must have
• Facebook and Instagram Logos. Contact Numbers.
Should not have
• Any Persons.

```html
<!DOCTYPE html>
<html lang="en">
<head>
<meta charset="UTF-8">
<title>Mistral Haze – Store Front Sign</title>
<link rel="stylesheet" href="https://fonts.googleapis.com/css2?family=Montserrat:wght@300;500&display=swap">
<style>
  :root {
    --page-bg: #e4e5e7;
    --sign-black: #070707;
    --sign-edge: #2a2a2c;
    --badge-fill: #3b3b3e;
    --badge-ring: #f2f2f2;
    --text-light: #e9e9e9;
    --divider: #5a5a5a;
  }
  * { box-sizing: border-box; margin: 0; padding: 0; }
  html, body {
    width: 1200px;
    height: 900px;
    overflow: hidden;
    background: var(--page-bg);
    font-family: "Montserrat", sans-serif;
  }
  .store-sign {
    position: absolute;
    left: 30px;
    top: 260px;
    width: 1140px;
    height: 380px;
    background: var(--sign-black);
    border: 3px solid var(--sign-edge);
  }
  .brand-badge {
    position: absolute;
    left: 320px;
    top: 30px;
    width: 300px;
    height: 300px;
    border-radius: 50%;
    background: var(--badge-fill);
    border: 7px solid var(--badge-ring);
    display: flex;
    align-items: center;
    justify-content: center;
  }
  .brand-name {
    color: var(--text-light);
    font-weight: 300;
    font-size: 42px;
    line-height: 1.15;
    text-align: center;
    letter-spacing: 1px;
  }
  .contact-numbers {
    position: absolute;
    left: 72px;
    bottom: 42px;
    display: flex;
    align-items: center;
    gap: 12px;
    color: var(--text-light);
    font-weight: 300;
    font-size: 19px;
    line-height: 1;
  }
  .contact-item { display: flex; align-items: center; gap: 8px; }
  .contact-divider { width: 1px; height: 22px; background: var(--divider); }
  .chat-mark {
    width: 14px; height: 14px; border-radius: 50%;
    border: 2px solid var(--text-light);
  }
  .social-handle {
    position: absolute;
    left: 722px;
    bottom: 88px;
    display: flex;
    align-items: center;
    gap: 14px;
    color: var(--text-light);
    font-weight: 300;
    font-size: 23px;
    line-height: 1;
  }
  .social-mark {
    width: 17px; height: 17px; border-radius: 3px;
    background: var(--text-light);
  }
  .social-handle .handle-text { margin-left: 4px; }
</style>
</head>
<body>
  <div class="store-sign">
    <div class="brand-badge">
      <p class="brand-name">Mistral<br>Haze</p>
    </div>

    <div class="contact-numbers">
      <div class="contact-item">
        <svg class="phone-icon" width="15" height="17" viewBox="0 0 24 24" aria-hidden="true">
          <path fill="#e9e9e9" d="M6.6 10.8a15.1 15.1 0 0 0 6.6 6.6l2.2-2.2a1 1 0 0 1 1-.25 11.4 11.4 0 0 0 3.6.57 1 1 0 0 1 1 1V20a1 1 0 0 1-1 1A17 17 0 0 1 3 4a1 1 0 0 1 1-1h3.5a1 1 0 0 1 1 1c0 1.25.2 2.45.57 3.57a1 1 0 0 1-.25 1z"/>
        </svg>
        <span>593-6148</span>
      </div>
      <span class="contact-divider"></span>
      <div class="contact-item">
        <span class="chat-mark"></span>
        <span>364-9105</span>
      </div>
    </div>

    <div class="social-handle">
      <span class="social-mark"></span>
      <span class="social-mark"></span>
      <span class="handle-text">@mistralhaze</span>
    </div>
  </div>
</body>
</html>
```